Website Design for Harborline Trade Hub! Buying Electronics Antiques Gold and valuables Online w/Cash

Our company gives people a reliable place to sell their old or un-needed valuables online where they can get a fair price and be involved in the decision upon the price to be paid. We provide prices for a huge variety of items ranging from Cell Phones, El

```html
<!DOCTYPE html>
<html lang="en">
<head>
<meta charset="utf-8">
<title>Harborline Trade Hub — Sell Your Valuables for Cash</title>
<link href="https://fonts.googleapis.com/css2?family=Arimo:wght@400;700&family=Lobster&family=Open+Sans:wght@400;600;700&family=PT+Sans+Narrow:wght@400;700&family=Tinos:ital@1&family=Ubuntu:wght@500;700&display=swap" rel="stylesheet">
<style>
:root{
  --red:#d63a3f;
  --red-dark:#b8262c;
  --red-deep:#8f1d22;
  --blue:#3b8fd3;
  --blue-light:#7cc0ee;
  --blue-dark:#1c6fb4;
  --navy:#24327a;
  --ink:#333;
  --ink-soft:#555;
  --paper:#fff;
  --rule:#ddd;
  --gold:#f0a21a;
}
*{box-sizing:border-box;margin:0;padding:0}
html,body{width:706px;height:1200px;overflow:hidden;background:var(--paper)}
body{position:relative;font-family:"Open Sans",sans-serif;color:var(--ink)}
.abs{position:absolute}
.top-rule{left:0;top:0;width:706px;height:2px;background:var(--red-deep)}
.brand{left:90px;top:14px;width:150px;font-family:"Ubuntu",sans-serif;font-weight:700;font-size:19px;line-height:20px;color:var(--navy)}
.account{left:524px;top:18px;display:flex;gap:4px}
.account a{width:28px;height:28px;border-radius:50%;background:radial-gradient(circle at 40% 35%,#ef5a5e,var(--red-dark));border:2px solid #f3c9ca;box-shadow:0 1px 2px rgba(0,0,0,.35);color:#fff;font-family:"PT Sans Narrow",sans-serif;font-size:6.5px;font-weight:700;white-space:nowrap;display:flex;align-items:center;justify-content:center;text-decoration:none}
.callout{left:470px;top:56px;font-family:"Tinos",serif;font-style:italic;font-size:13px;color:#444;white-space:nowrap}
.main-nav{left:90px;top:83px;width:526px;height:22px;background:linear-gradient(#5ab0ea,var(--blue-dark));border-radius:3px;display:flex;align-items:center;padding-left:5px}
.main-nav a{color:#fff;font-family:"Arimo",sans-serif;font-size:7px;text-decoration:none;padding:5px 8px;margin-right:12px}
.main-nav a.active{background:var(--red);border-radius:2px;padding:5px 8px}
.hero-band{left:0;top:147px;width:706px;height:127px;background:linear-gradient(#e04448,#c22d33)}
.hero-panel{left:90px;top:119px;width:526px;height:181px;background:linear-gradient(#9fd2f3,#3d93d6);border-radius:3px;box-shadow:0 3px 6px rgba(0,0,0,.3)}
.hero-title{left:90px;top:131px;width:526px;text-align:center;font-family:"Ubuntu",sans-serif;font-weight:700;font-size:27px;color:#3a3a3a;text-shadow:0 1px 0 #d9eefb}
.hero-lede{left:90px;top:168px;width:526px;text-align:center;font-family:"Arimo",sans-serif;font-size:6.5px;line-height:9px;color:#222}
.search{left:206px;top:193px;width:294px;height:53px;background:var(--red);border-radius:4px;box-shadow:0 2px 4px rgba(0,0,0,.3)}
.search-input{left:219px;top:202px;width:206px;height:30px;background:#fff;border-radius:2px;font-family:"Arimo",sans-serif;font-size:8px;letter-spacing:1px;color:#aaa;padding:10px 10px}
.search-btn{left:433px;top:203px;width:59px;height:29px;background:linear-gradient(#b0282e,#7d1a1f);border-radius:2px;color:#fff;font-size:10px;display:flex;align-items:center;justify-content:center}
.hero-mark{left:540px;top:218px;width:62px;height:72px;border:2px solid rgba(255,255,255,.55);border-radius:2px}
.hero-note{left:132px;top:265px;font-family:"Arimo",sans-serif;font-size:6.5px;color:#222}
.hero-note::before{content:"";display:inline-block;width:4px;height:4px;border-radius:50%;background:var(--red-deep);margin-right:5px;vertical-align:middle}
.section-title{font-family:"PT Sans Narrow",sans-serif;font-weight:700;color:var(--red)}
.how-title{left:89px;top:323px;font-size:20px}
.diagram{left:0;top:0;width:706px;height:1200px;pointer-events:none}
.step-art{border-radius:8px}
.step-text{font-family:"Arimo",sans-serif;font-size:6px;line-height:10px;color:#333;text-align:center}
.about-title{left:89px;top:684px;font-size:17px}
.about-copy{left:89px;top:718px;width:340px;font-size:6.4px;line-height:12.6px;color:#444}
.items-title{left:89px;top:793px;font-size:15px}
.item{top:829px;width:80px}
.item .photo{width:80px;height:94px}
.item p{margin-top:5px;text-align:center;font-size:8px;color:#333}
.testimonials{left:455px;top:676px;width:162px;height:158px;border:1px solid var(--rule);border-radius:3px;background:#fff;box-shadow:0 1px 3px rgba(0,0,0,.12);overflow:hidden}
.testimonials h3{height:26px;background:var(--red);color:#fff;font-family:"PT Sans Narrow",sans-serif;font-weight:700;font-size:15px;text-align:center;line-height:26px}
.quote{position:absolute;left:6px;width:148px;display:flex;gap:5px}
.quote .thumb{width:34px;height:34px;flex:none;border-radius:2px}
.quote .who{display:flex;justify-content:space-between;font-size:6px;font-weight:700;letter-spacing:.5px;color:#444}
.quote .said{font-size:5.4px;line-height:9px;color:#555;margin-top:2px}
.quote-rule{position:absolute;left:12px;width:138px;height:1px;background:var(--rule)}
.read-more{position:absolute;right:13px;bottom:6px;font-size:6px;font-weight:700;color:var(--blue-dark)}
.promo{left:455px;top:844px;width:162px;height:89px;background:radial-gradient(circle at 60% 40%,#d83c41,#a5232a);border:1px solid #8d1c21}
.promo h4{position:absolute;left:10px;top:8px;font-family:"Lobster",cursive;font-weight:400;font-size:11px;color:var(--gold);white-space:nowrap}
.promo p{position:absolute;left:14px;top:28px;width:140px;font-size:6.4px;line-height:9px;color:#fde}
.promo .cta{position:absolute;left:41px;top:67px;width:80px;height:11px;border-radius:6px;background:linear-gradient(#ffc04a,#e5810c);color:#8a3a06;font-size:5.5px;font-weight:700;letter-spacing:.5px;text-align:center;line-height:11px}
.footer-band{left:0;top:1017px;width:706px;height:108px;background:linear-gradient(#3aa0e6,var(--blue-dark))}
.footer-panel{left:90px;top:992px;width:526px;height:139px;background:linear-gradient(#e0474b,#c0292f);box-shadow:0 3px 6px rgba(0,0,0,.3)}
.footer-bar{left:103px;top:1002px;width:498px;height:16px;background:var(--red-dark)}
.footer-col{top:1005px}
.footer-col h5{font-family:"Arimo",sans-serif;font-size:6.3px;font-weight:700;letter-spacing:.6px;color:#fff;margin-bottom:14px}
.footer-col li{list-style:none;font-family:"Arimo",sans-serif;font-size:6px;line-height:12.8px;color:#fff;white-space:nowrap}
.social{display:grid;grid-template-columns:repeat(3,16px);gap:9px 8px;margin-top:-2px}
.social span{width:16px;height:16px;border-radius:3px;background:#e9eef3;box-shadow:0 1px 2px rgba(0,0,0,.3)}
.basket{left:527px;top:1088px;width:75px;height:64px;border-radius:4px}
.foot-brand{left:93px;top:1142px;width:100px;font-family:"Ubuntu",sans-serif;font-weight:700;font-size:11px;line-height:12px;color:var(--navy)}
.seals{left:251px;top:1142px;display:flex;gap:5px;align-items:center}
.seal{background:#d6d6d6}
.copyright{left:198px;top:1172px;font-family:"Arimo",sans-serif;font-size:5.6px;color:#555;white-space:nowrap}
.bottom-rule{left:0;top:1196px;width:706px;height:4px;background:#3a3a3a}
</style>
</head>
<body>
<div class="abs top-rule"></div>

<header>
  <div class="abs brand">Harborline<br>Trade Hub</div>
  <nav class="abs account"><a href="#">Log In</a><a href="#">Sign Up</a><a href="#">Help</a></nav>
  <div class="abs callout">Call Us Now&nbsp; 555-0142-00</div>
  <nav class="abs main-nav">
    <a class="active" href="#">HOME</a><a href="#">HOW IT WORKS</a><a href="#">BUSINESS BUYBACK</a><a href="#">FUNDRAISING</a><a href="#">BLOG</a><a href="#">CONTACT</a><a href="#">HELP</a>
  </nav>
</header>

<section class="hero">
  <div class="abs hero-band"></div>
  <div class="abs hero-panel"></div>
  <h1 class="abs hero-title">SELL YOUR VALUABLES FOR CASH</h1>
  <p class="abs hero-lede">Lorem Ipsum is simply dummy text of the printing and typesetting industry.<br>Lorem Ipsum has been the industry's standard dummy text ever since the 1500s,</p>
  <div class="abs search"></div>
  <div class="abs search-input">Enter Your Text Here ...</div>
  <div class="abs search-btn">SEARCH</div>
  <div class="abs hero-mark"></div>
  <p class="abs hero-note">Lorem Ipsum is simply dummy text of the printing and typesetting industry</p>
</section>

<section class="how">
  <h2 class="abs section-title how-title">How It Works</h2>
  <svg class="abs diagram" viewBox="0 0 706 1200" aria-hidden="true">
    <defs>
      <marker id="head" viewBox="0 0 10 10" refX="8" refY="5" markerWidth="7" markerHeight="7" orient="auto"><path d="M0 0L10 5L0 10z" fill="#c0282e"/></marker>
    </defs>
    <path d="M236 393 Q360 340 474 392" fill="none" stroke="#d63a3f" stroke-width="2" marker-end="url(#head)"/>
    <path d="M486 488 L469 491" fill="none" stroke="#d63a3f" stroke-width="2" marker-end="url(#head)"/>
    <circle cx="183" cy="432" r="59" fill="#fff" stroke="#1c7fc4" stroke-width="4"/>
    <circle cx="532" cy="432" r="59" fill="#fff" stroke="#1c7fc4" stroke-width="4"/>
    <circle cx="363" cy="519" r="101" fill="#fff" stroke="#d63a3f" stroke-width="4"/>
  </svg>
  <div class="abs step-art" role="img" aria-label="Desktop computer illustration" style="left:152px;top:402px;width:62px;height:58px;background:linear-gradient(#cfe4f5,#8fb3d1)"></div>
  <div class="abs step-art" role="img" aria-label="Stacked shipping boxes on a pallet" style="left:499px;top:404px;width:66px;height:56px;background:linear-gradient(#f07a4a,#b8432a)"></div>
  <div class="abs step-art" role="img" aria-label="Stack of coins on banknotes" style="left:298px;top:446px;width:130px;height:124px;background:linear-gradient(#dfe3e4,#a9b89c)"></div>
  <p class="abs step-text" style="left:118px;top:499px;width:130px">Lorem Ipsum is simply dummy text of the printing and typesetting industry. Lorem Ipsum has been the industry.</p>
  <p class="abs step-text" style="left:467px;top:499px;width:130px">Lorem Ipsum is simply dummy text of the printing and typesetting industry. Lorem Ipsum has been the industry.</p>
  <p class="abs step-text" style="left:273px;top:623px;width:180px">Lorem Ipsum is simply dummy text of the printing and type-setting industry. Lorem Ipsum has been the industry.</p>
</section>

<section class="about">
  <h2 class="abs section-title about-title">About</h2>
  <p class="abs about-copy">Lorem Ipsum is simply dummy text of the printing and typesetting industry. Lorem Ipsum has been the industry's standard dummy text ever since the 1500s, when an unknown printer took a galley of type and scrambled it to make a type specimen book. It has survived not only five centuries, but also the leap into electronic typesetting, remaining essentially unchanged.</p>
  <h2 class="abs section-title items-title">TOP RESENT ITEMS</h2>
  <figure class="abs item" style="left:89px"><div class="photo" role="img" aria-label="Laptop photo" style="background:linear-gradient(160deg,#9fb8cc,#3a4048 60%,#1f2226)"></div><p>Laptop</p></figure>
  <figure class="abs item" style="left:173px"><div class="photo" role="img" aria-label="Hand holding a cell phone" style="background:linear-gradient(160deg,#e2dcd4,#8a7e74 55%,#3e3a36)"></div><p>Cell Phone</p></figure>
  <figure class="abs item" style="left:259px"><div class="photo" role="img" aria-label="Gold bangles" style="background:linear-gradient(160deg,#4a3a10,#e9c33a 40%,#a8770f)"></div><p>Gold</p></figure>
  <figure class="abs item" style="left:343px"><div class="photo" role="img" aria-label="Gold jewelry necklace set" style="background:linear-gradient(180deg,#f6efe4,#c79a4a 50%,#8a3a2a)"></div><p>Jewelry</p></figure>
</section>

<aside class="abs testimonials">
  <h3>Testamonials</h3>
  <div class="quote" style="top:34px"><div class="thumb" role="img" aria-label="Red compact camera" style="background:linear-gradient(#e05050,#7d2a2a)"></div><div style="flex:1"><div class="who"><span>DANA MORROW</span><span>$64</span></div><p class="said">Lorem Ipsum is simply dummy text of the printing and typesetting industry.</p></div></div>
  <div class="quote-rule" style="top:77px"></div>
  <div class="quote" style="top:91px"><div class="thumb" role="img" aria-label="Smartphone in hand" style="background:linear-gradient(#7a7a7a,#d9b9a8)"></div><div style="flex:1"><div class="who"><span>DANA MORROW</span><span>$55</span></div><p class="said">Lorem Ipsum is simply dummy text of the printing and typesetting industry.</p></div></div>
  <div class="quote-rule" style="top:134px"></div>
  <span class="read-more">Read More</span>
</aside>

<aside class="abs promo">
  <h4>Cell Your valuables For Cash!!</h4>
  <p>Lorem Ipsum is simply dummy text of the printing and typesetting industry.</p>
  <div class="cta">GET STARTED</div>
</aside>

<footer>
  <div class="abs footer-band"></div>
  <div class="abs footer-panel"></div>
  <div class="abs footer-bar"></div>
  <div class="abs footer-col" style="left:109px"><h5>ABOUT HTH</h5><ul><li>Media Center</li><li>Tidewater For Good</li><li>Privacy Policy</li><li>Your CA Privacy Rights</li><li>Terms of Use</li><li>General Policies</li><li>Intellectual Property Rights</li></ul></div>
  <div class="abs footer-col" style="left:218px"><h5>RESOURCES</h5><ul><li>Site Map</li><li>Mobile</li><li>Publishers</li><li>Brand Partners</li><li>Join Our Affiliate Program</li><li>Flashcards App</li></ul></div>
  <div class="abs footer-col" style="left:332px"><h5>COMPANY</h5><ul><li>Management</li><li>Blog</li><li>Jobs</li><li>Customer Service</li><li>Give Us Feedback</li></ul></div>
  <div class="abs footer-col" style="left:469px"><h5>FOLLOW US</h5><div class="social"><span></span><span></span><span></span><span></span><span></span></div></div>
  <div class="abs basket" role="img" aria-label="Blue basket filled with gadgets" style="background:linear-gradient(#e4e4e4,#3a6fd0)"></div>
  <div class="abs foot-brand">Harborline<br>Trade Hub</div>
  <div class="abs seals">
    <span class="seal" style="width:20px;height:20px;border-radius:50%;background:#e2cf7a"></span>
    <span class="seal" style="width:18px;height:20px;border-radius:3px"></span>
    <span class="seal" style="width:20px;height:20px;border-radius:50%"></span>
    <span class="seal" style="width:66px;height:20px;border-radius:2px;background:#cfd9e6"></span>
    <span style="width:8px"></span>
    <span class="seal" style="width:62px;height:16px;border-radius:2px;background:#d9e8cf"></span>
  </div>
  <p class="abs copyright">Copyright 2012 Keelson, LLC All Rights Reserved • Privacy Policy • Environmental Awareness • Terms &amp; Conditions</p>
  <div class="abs bottom-rule"></div>
</footer>
</body>
</html>
```